Postcard Design

Company Name--motion harbor
482 Garnet Avenue
Brooklyn New York11231
347-555-0182
www.motionharbors. example
We are a boutique personal fitness company in a exclusive neighnorhood in Brooklyn New York. We specialize in personal training and innovate new fitness classes such as Pulse-Circuit QVR and Tabata.

We want our brand to be high-end but open to all. Laid-back but experts in the field of fitness. Innovative and flexible. Proffessional, friendly and inspiring.

Personal attention for our clients is a must as well as making sure they succeed. 87% of our clients reach their goals.

Colors should be bright but sophisticated with a little aggression but not intimidation.
Updates

Company Name-And contact info has been updated on the brief

I posted a logo. And the colors on the website have changed. If you could incorporate the website color scheme that would be helpful. If for whatever reason the logo is not here I will try to upload again.

Change the contact info: www.motionharbors.example You tube: Brisco and the Motion Harbor Email: Motionharbors@mailbox.example Verbiage changes: 'The only boutique personal fitness studio in Brooklyn. Featuring uniquely proprietary classes QVR, Cross Training and now Tabata." Verbiage Additions Safe for moms, dads and we offer enhanced childcare with certified child care development teachers with our partner studios. Classes start at $15

Please Add : Use this postcard to receive 10% any service

Hi, I could not upload the logo. However they said that our Logo should be uploaded now as I sent it to them manually.

Target Market(s)

30-40 year old women and new moms looking to do cross fit and personal training. Income 80-85K.

Industry/Entity Type

Boutique

Requirements
Must have
• Highlight Tabata and the excellence of the classes.Tag lines- Increase calorie burn by 20%. Increase muscle tone by 25%.Increase metabolism by 25%. Classes only available by appointment. 30mins or 1 hour.
Nice to have
• Attractive and fit young people having fun. Personal training.
Should not have
• Overly sexual fitness models.

```html
<!DOCTYPE html>
<html lang="en">
<head>
<meta charset="utf-8">
<title>Motion Harbor Postcard</title>
<link rel="stylesheet" href="https://fonts.googleapis.com/css2?family=Arimo:wght@400;700&display=swap">
<style>
  :root {
    --stage: #8a8a8a;
    --stage-light: #b4b4b4;
    --purple: #a1399b;
    --purple-dark: #8a2f86;
    --green: #8cc63f;
    --card-back: #f8f2f5;
    --ink: #4a4a4a;
    --line: #7a7a7a;
    --white: #ffffff;
  }
  * { box-sizing: border-box; margin: 0; padding: 0; }
  html, body { width: 1200px; height: 900px; overflow: hidden; }
  body {
    background: radial-gradient(ellipse at 50% 45%, var(--stage-light), var(--stage));
    font-family: "Arimo", Arial, sans-serif;
    position: relative;
  }
  .postcard {
    position: absolute;
    width: 600px;
    height: 410px;
    box-shadow: 0 10px 24px rgba(0,0,0,0.35);
    overflow: hidden;
  }

  /* Front side */
  .postcard--front { left: 40px; top: 70px; background: var(--white); }
  .collage {
    position: absolute; inset: 0;
    display: grid;
    grid-template-columns: repeat(4, 1fr);
    grid-template-rows: repeat(3, 1fr);
    gap: 4px;
    background: var(--white);
  }
  .collage__tile { display: block; }
  .tile--trainer { grid-column: 1 / 3; background: linear-gradient(135deg, #dfe3ea, #9aa3b3); }
  .tile--dumbbells { grid-column: 3 / 4; background: linear-gradient(135deg, #c9cdd6, #6e7584); }
  .tile--core { grid-column: 4 / 5; background: linear-gradient(135deg, #e7c7a8, #2e2f3a); }
  .tile--lifting { grid-column: 1 / 2; background: linear-gradient(135deg, #e6e2e8, #9c5fa8); }
  .tile--curl { grid-column: 2 / 4; background: linear-gradient(135deg, #f0ddc9, #b98a6a); }
  .tile--smile { grid-column: 4 / 5; background: linear-gradient(135deg, #d9e6ef, #8fb6d0); }
  .tile--floor { grid-column: 1 / 2; background: linear-gradient(135deg, #d5d7dd, #8c93a3); }
  .tile--run { grid-column: 2 / 4; background: linear-gradient(135deg, #c9ced8, #5a6172); }
  .tile--gym { grid-column: 4 / 5; background: linear-gradient(135deg, #ececec, #a7adb8); }
  .headline-band {
    position: absolute;
    left: 0; top: 178px;
    width: 380px; height: 118px;
    background: var(--purple);
    color: var(--white);
    padding: 18px 22px;
  }
  .headline-band__title { font-size: 25px; font-weight: 400; line-height: 1.12; }
  .headline-band__sub { font-size: 15px; margin-top: 8px; }

  /* Back side */
  .postcard--back { left: 560px; top: 420px; background: var(--card-back); }
  .back__info { position: absolute; left: 0; top: 0; width: 330px; height: 100%; }
  .brand {
    position: absolute; left: 22px; top: 22px;
    display: flex; align-items: center; gap: 10px;
  }
  .brand__mark { width: 14px; height: 14px; border-radius: 50%; background: var(--green); }
  .brand__name { font-size: 34px; font-weight: 700; color: var(--purple); }
  .tagline { position: absolute; left: 22px; top: 74px; font-size: 13px; color: var(--ink); }
  .benefits {
    position: absolute; left: 0; top: 98px;
    width: 330px; height: 86px;
    background: var(--purple);
    color: var(--white);
    padding: 10px 22px;
    font-weight: 700; font-size: 15.5px; line-height: 1.42;
  }
  .booking { position: absolute; left: 22px; top: 198px; width: 290px; display: flex; align-items: center; gap: 12px; }
  .booking__note { font-size: 13.5px; color: var(--ink); line-height: 1.25; width: 96px; }
  .duration { display: flex; flex-direction: column; align-items: center; gap: 3px; font-weight: 700; font-size: 13px; }
  .duration--short { color: var(--green); }
  .duration--long { color: var(--purple); }
  .booking__or { font-weight: 700; font-size: 18px; color: var(--ink); }
  .contact { position: absolute; left: 22px; top: 292px; list-style: none; }
  .contact__item { display: flex; align-items: center; gap: 8px; font-size: 13.5px; font-weight: 700; color: var(--ink); margin-bottom: 7px; }
  .contact__icon { width: 16px; height: 16px; flex: none; }
  .back__address { position: absolute; left: 350px; top: 26px; width: 226px; height: 250px; border-left: 1px solid var(--line); padding-left: 16px; }
  .address__label { font-size: 13px; color: var(--ink); }
  .address__line { border-bottom: 1px solid var(--line); height: 54px; }
</style>
</head>
<body>
  <section class="postcard postcard--front">
    <div class="collage">
      <div class="collage__tile tile--trainer" role="img" aria-label="Photo of a trainer coaching a client at the gym"></div>
      <div class="collage__tile tile--dumbbells" role="img" aria-label="Photo of a hand lifting a dumbbell from a rack"></div>
      <div class="collage__tile tile--core" role="img" aria-label="Photo of a toned midsection"></div>
      <div class="collage__tile tile--lifting" role="img" aria-label="Photo of a woman lifting a barbell"></div>
      <div class="collage__tile tile--curl" role="img" aria-label="Photo of a man curling a dumbbell"></div>
      <div class="collage__tile tile--smile" role="img" aria-label="Photo of a smiling woman with a towel after a workout"></div>
      <div class="collage__tile tile--floor" role="img" aria-label="Photo of gym equipment"></div>
      <div class="collage__tile tile--run" role="img" aria-label="Photo of running shoes on a treadmill"></div>
      <div class="collage__tile tile--gym" role="img" aria-label="Photo of a bright gym interior"></div>
    </div>
    <div class="headline-band">
      <h1 class="headline-band__title">The boutique personal fitness training classes.</h1>
      <p class="headline-band__sub">Such as Pulse-Circuit QVR and Tabata.</p>
    </div>
  </section>

  <section class="postcard postcard--back">
    <div class="back__info">
      <div class="brand">
        <span class="brand__mark"></span>
        <span class="brand__name">Motion Harbor</span>
      </div>
      <p class="tagline">Tabata and the excellence of the classes.</p>
      <div class="benefits">
        <p>Increase calorie burn by 20%.</p>
        <p>Increase muscle tone by 25%.</p>
        <p>Increase metabolism by 25%.</p>
      </div>
      <div class="booking">
        <p class="booking__note">Classes only available by appointment.</p>
        <div class="duration duration--short">
          <svg width="40" height="40" viewBox="0 0 40 40"><circle cx="20" cy="20" r="17" fill="none" stroke="#8cc63f" stroke-width="3"/><path d="M20 20 L20 9 M20 20 L28 24" stroke="#8cc63f" stroke-width="3" stroke-linecap="round"/></svg>
          <span>30mins</span>
        </div>
        <span class="booking__or">or</span>
        <div class="duration duration--long">
          <svg width="40" height="40" viewBox="0 0 40 40"><circle cx="20" cy="20" r="17" fill="none" stroke="#a1399b" stroke-width="3"/><path d="M20 20 L20 9 M20 20 L12 26" stroke="#a1399b" stroke-width="3" stroke-linecap="round"/></svg>
          <span>1 hour</span>
        </div>
      </div>
      <ul class="contact">
        <li class="contact__item">
          <svg class="contact__icon" viewBox="0 0 16 16"><path d="M8 1a5 5 0 0 0-5 5c0 4 5 9 5 9s5-5 5-9a5 5 0 0 0-5-5z" fill="#a1399b"/><circle cx="8" cy="6" r="2" fill="#fff"/></svg>
          #482 Garnet Avenue, Brooklyn New York 11231
        </li>
        <li class="contact__item">
          <svg class="contact__icon" viewBox="0 0 16 16"><rect x="1" y="3" width="14" height="10" rx="1" fill="#a1399b"/><path d="M1.5 4 L8 9 L14.5 4" fill="none" stroke="#fff" stroke-width="1.3"/></svg>
          info@motionharbors.example
        </li>
        <li class="contact__item">
          <svg class="contact__icon" viewBox="0 0 16 16"><circle cx="8" cy="8" r="7" fill="#a1399b"/><path d="M1 8h14M8 1c-3 3-3 11 0 14M8 1c3 3 3 11 0 14" fill="none" stroke="#fff" stroke-width="1"/></svg>
          www.motionharbors.example
        </li>
        <li class="contact__item">
          <svg class="contact__icon" viewBox="0 0 16 16"><circle cx="8" cy="8" r="7" fill="#a1399b"/><path d="M5.5 4.5c-1 1 0 4 2 6s5 3 6 2l-1.5-1.5-1.5 1c-1-.5-2.5-2-3-3l1-1.5z" fill="#fff"/></svg>
          347-555-0182
        </li>
      </ul>
    </div>
    <div class="back__address">
      <p class="address__label">AddressArea</p>
      <div class="address__line"></div>
      <div class="address__line"></div>
      <div class="address__line"></div>
    </div>
  </section>
</body>
</html>
```